Natural Cosmetics need a Packaging Design

We need a PACKAGING design for labels on hand/body wash bottles and soap paper boxes.
We target at high end markets.
We expect a contemporary and trendy design.
We don't need a separate logo. The brand name "Ma Vitrine" acts as the logo.
We want a modern and classic font for "Ma Vitrine".
Please see attached pictures for packaging samples.

Industry/Entity Type

Cosmetics

Requirements
Should not have
• a separate logo from the brand name

```html
<!DOCTYPE html>
<html lang="en">
<head>
<meta charset="UTF-8">
<title>Ma Vitrine – Hands &amp; Body Wash Label</title>
<link rel="stylesheet" href="https://fonts.googleapis.com/css2?family=Raleway:wght@300;400;500&display=swap">
<style>
  :root {
    --page-bg: #ffffff;
    --label-bg: #ffffff;
    --label-edge: #e6eaee;
    --brand-blue: #1c5ea6;
    --rule-blue: #3f7fc0;
    --teal: #27a3b6;
    --teal-soft: #3c9bc0;
    --leaf-green: #8cc63f;
    --wave-light: #d6ecf8;
    --wave-mid: #6cc0ec;
    --wave-deep: #1f8fd6;
  }
  * { margin: 0; padding: 0; box-sizing: border-box; }
  html, body {
    width: 1200px;
    height: 1200px;
    overflow: hidden;
    background: var(--page-bg);
  }
  .canvas {
    position: relative;
    width: 1200px;
    height: 1200px;
  }
  .label {
    position: absolute;
    left: 202px;
    top: 85px;
    width: 796px;
    height: 1030px;
    background: var(--label-bg);
    border: 1px solid var(--label-edge);
    border-radius: 22px;
    overflow: hidden;
    font-family: "Raleway", sans-serif;
    text-align: center;
  }
  .brand {
    position: absolute;
    top: 72px;
    left: 0;
    width: 100%;
    font-size: 82px;
    font-weight: 400;
    letter-spacing: 10px;
    text-transform: uppercase;
    color: var(--brand-blue);
    line-height: 1;
  }
  .brand-rule {
    position: absolute;
    top: 166px;
    left: 60px;
    width: 676px;
    height: 2px;
    background: var(--rule-blue);
  }
  .product-type {
    position: absolute;
    top: 268px;
    left: 0;
    width: 100%;
    font-size: 46px;
    font-weight: 400;
    color: var(--teal-soft);
    line-height: 1;
  }
  .product-name {
    position: absolute;
    top: 322px;
    left: 0;
    width: 100%;
    font-size: 106px;
    font-weight: 300;
    color: var(--teal);
    line-height: 0.84;
    letter-spacing: -3px;
  }
  .product-name .amp { color: var(--leaf-green); }
  .product-note {
    position: absolute;
    top: 520px;
    left: 0;
    width: 100%;
    font-size: 24px;
    font-weight: 400;
    color: var(--leaf-green);
    line-height: 1;
  }
  .wave-art {
    position: absolute;
    left: 0;
    bottom: 0;
    width: 100%;
    height: 470px;
    background: linear-gradient(180deg,
      rgba(255,255,255,0) 0%,
      var(--wave-light) 30%,
      var(--wave-mid) 65%,
      var(--wave-deep) 100%);
  }
</style>
</head>
<body>
  <main class="canvas">
    <section class="label">
      <div class="brand">Ma Vitrine</div>
      <div class="brand-rule"></div>
      <p class="product-type">moisture</p>
      <h1 class="product-name">HANDS<span class="amp">&amp;</span><br>BODY WASH</h1>
      <p class="product-note">with vitamin e</p>
      <div class="wave-art" role="img" aria-label="Flowing abstract blue light waves"></div>
    </section>
  </main>
</body>
</html>
```